Brivello corporate flyer design for a Technology company

We need to design a flyer for our company.

Please find specs in the attached files in this link: https://files.quandrel-docs.example/document/d/7XkPqLmZrT2vWnB8cHdYs4FgJuEaQoRiNtVb3MzKlC9/edit?tab=t.pqrmzvlotgha

We also add some additional files for you to use

Font styles to use
Other font styles liked:
• Google Sans

```html
<!DOCTYPE html>
<html lang="en">
<head>
<meta charset="utf-8">
<title>Brivello Flyer</title>
<link rel="stylesheet" href="https://fonts.googleapis.com/css2?family=Poppins:ital,wght@0,400;0,500;0,600;0,700;1,700;1,800&display=swap">
<style>
  :root {
    --navy-deep: #0a1a36;
    --navy: #10284f;
    --navy-teal: #0f4a5c;
    --teal: #1ea89b;
    --ink: #14213a;
    --white: #ffffff;
    --stage-light: #ffffff;
    --stage-teal: #8cc7bf;
  }
  * { margin: 0; padding: 0; box-sizing: border-box; }
  html, body { width: 1200px; height: 2582px; overflow: hidden; }
  body {
    position: relative;
    font-family: "Poppins", sans-serif;
    background: linear-gradient(to bottom, var(--stage-light) 0, var(--stage-light) 1465px, var(--stage-teal) 1465px, #b3e0d9 100%);
  }
  .flyer {
    position: absolute; left: 149px; top: 158px;
    width: 911px; height: 1180px;
    background: var(--white);
    box-shadow: 0 20px 60px rgba(0,0,0,0.18);
    overflow: hidden;
  }
  .hero {
    position: absolute; left: 0; top: 0; width: 911px; height: 980px;
    background: radial-gradient(ellipse at 70% 85%, var(--navy-teal) 0, transparent 55%),
                linear-gradient(160deg, var(--navy) 0%, var(--navy-deep) 60%, #0c2a48 100%);
  }
  .hero-curve { position: absolute; left: 0; top: 940px; width: 911px; height: 60px; }
  .portrait {
    position: absolute; left: 600px; top: 125px; width: 311px; height: 830px;
    background: linear-gradient(180deg, rgba(40,60,100,0) 0%, #1c3566 25%, #203e78 60%, #142a55 100%);
    border-radius: 140px 0 0 0;
  }
  .brand {
    position: absolute; left: 77px; top: 62px;
    display: flex; align-items: center; gap: 10px;
    color: var(--white); font-weight: 600; font-size: 44px; letter-spacing: -0.5px;
  }
  .brand-mark { width: 30px; height: 30px; background: var(--teal); }
  .headline {
    position: absolute; left: 75px; top: 150px;
    color: var(--white); font-weight: 700; font-size: 100px; line-height: 100px; letter-spacing: -1px;
  }
  .subhead {
    position: absolute; left: 77px; top: 443px;
    color: var(--white); font-weight: 700; font-size: 50px; letter-spacing: -0.3px;
  }
  .rule { position: absolute; left: 78px; top: 510px; width: 272px; height: 4px; background: var(--white); border-radius: 2px; }
  .intro {
    position: absolute; left: 77px; top: 528px; width: 640px;
    color: var(--white); font-size: 22px; line-height: 39px;
  }
  .intro em { font-weight: 700; font-style: italic; }
  .pill {
    position: absolute; height: 87px;
    border: 2px solid var(--white); border-radius: 22px;
    color: var(--white); font-size: 16px; line-height: 21px;
    display: flex; align-items: center; padding: 0 26px;
  }
  .pill--solid { background: var(--white); color: var(--ink); font-weight: 500; padding: 0 24px; }
  .stats {
    position: absolute; left: 79px; top: 992px; width: 560px;
    color: var(--ink); font-size: 22px; line-height: 33px;
  }
  .pain-list { position: absolute; left: 68px; top: 1070px; display: flex; gap: 22px; align-items: center; }
  .pain { display: flex; align-items: center; gap: 8px; color: var(--teal); font-weight: 600; font-size: 22px; }
  .pain svg { width: 60px; height: 62px; }
  .divider { position: absolute; left: 651px; top: 992px; width: 2px; height: 150px; background: var(--ink); }
  .promise {
    position: absolute; left: 697px; top: 995px;
    color: var(--ink); font-weight: 600; font-size: 22px; line-height: 33px;
  }
</style>
</head>
<body>
  <article class="flyer">
    <section class="hero">
      <div class="portrait" role="img" aria-label="Photo of a businessman in a navy suit looking at a tablet"></div>
      <div class="brand"><span class="brand-mark"></span>Brivello</div>
      <h1 class="headline">Data<br>Analytics<br>&amp; AI</h1>
      <p class="subhead">for Nonconformists</p>
      <div class="rule"></div>
      <p class="intro">If you have perfect control of your data,&nbsp; AI doesn't apply to you,&nbsp; and your company is bursting with talent<br><em>well done!</em><br>For everyone else, <em>we're your partner!</em></p>
      <div class="pill" style="left:79px;top:720px;width:223px;">Be impressed by our Exceptional Results</div>
      <div class="pill" style="left:328px;top:720px;width:297px;">Gain peace of mind with our Expert Partner</div>
      <div class="pill" style="left:79px;top:834px;width:416px;">Discover the thrill of innovation in a dynamic and collaborative environment</div>
      <div class="pill pill--solid" style="left:519px;top:834px;width:120px;">Have fun with us!</div>
    </section>
    <svg class="hero-curve" viewBox="0 0 911 60" preserveAspectRatio="none" aria-hidden="true">
      <path d="M0 60 L0 28 Q0 12 40 12 L871 12 Q911 12 911 28 L911 0 L911 60 Z" fill="#ffffff"/>
    </svg>

    <p class="stats">More than half of companies believe their providers don't fulfill on agreed terms, leading to</p>
    <div class="pain-list">
      <div class="pain">
        <svg viewBox="0 0 60 62" aria-hidden="true">
          <circle cx="30" cy="20" r="9" fill="#1ea89b"/>
          <path d="M8 18 L20 30 L40 30 L52 18 L56 22 L44 36 L40 36 L40 62 L20 62 L20 36 L16 36 L4 22 Z" fill="#1ea89b"/>
          <path d="M30 2 V7 M18 6 L21 10 M42 6 L39 10" stroke="#1ea89b" stroke-width="3" stroke-linecap="round"/>
        </svg>Frustration
      </div>
      <div class="pain">
        <svg viewBox="0 0 60 62" aria-hidden="true">
          <circle cx="29" cy="31" r="25" fill="none" stroke="#1ea89b" stroke-width="4"/>
          <circle cx="29" cy="31" r="19" fill="#1ea89b"/>
          <path d="M29 18 V31 L20 38" stroke="#fff" stroke-width="3" fill="none" stroke-linecap="round"/>
          <path d="M42 38 L54 60 L30 60 Z" fill="#1ea89b" stroke="#fff" stroke-width="2"/>
          <path d="M42 45 V53 M42 56 V57" stroke="#fff" stroke-width="3" stroke-linecap="round"/>
        </svg>Delays
      </div>
      <div class="pain">
        <svg viewBox="0 0 74 62" aria-hidden="true" style="width:72px">
          <circle cx="30" cy="31" r="28" fill="#1ea89b"/>
          <text x="30" y="44" text-anchor="middle" font-family="Poppins, sans-serif" font-weight="700" font-size="36" fill="#fff">$</text>
          <rect x="58" y="22" width="14" height="9" rx="4" fill="#1ea89b"/>
          <rect x="58" y="34" width="14" height="9" rx="4" fill="#1ea89b"/>
          <rect x="58" y="46" width="14" height="9" rx="4" fill="#1ea89b"/>
        </svg>Costs
      </div>
    </div>
    <div class="divider"></div>
    <p class="promise">At<br>Brivello,<br>We Deliver<br>Our Promises!</p>
  </article>
</body>
</html>
```